Plakat-Design für Immobilienmakler und Baufinanzierer
Zielgruppe
Wir sind Immobilienmakler und Baufinanzierer und suchen ein hochwertiges Design, unsere Zielgruppe sind Kunden, die Ihr Haus verkaufen möchten. Für jeden erfolgreichen Verkauf spenden wir 5 % unserer Maklercourtage an einen Verein, den sich der Kunde aussuchen darf. Mit diesem Plakat wollen wir auf unsere Vereinsförderng aufmerksam machen und Vereine ansprechen.
Aufgabenstellung
Text: 'Wir spenden 5 % unserer Provision für Ihren Verein', 'Nur 1,99 % Maklercourtage', Logo, Kontaktdaten

```html
<!DOCTYPE html>
<html lang="de">
<head>
<meta charset="utf-8">
<title>Vereinsförderung Plakat</title>
<link href="https://fonts.googleapis.com/css2?family=Montserrat:wght@500;600;700;800;900&display=swap" rel="stylesheet">
<style>
:root{
  --teal:#1e7488;
  --teal-soft:#b9dfea;
  --grey:#7f7f84;
  --red:#8c2229;
  --red-light:#d9363f;
  --sky:#29aee6;
  --sky-pale:#dff2fb;
  --white:#ffffff;
  --stage:#e9e9ea;
}
*{margin:0;padding:0;box-sizing:border-box}
html,body{width:1200px;height:1177px;overflow:hidden;background:var(--stage);font-family:'Montserrat',sans-serif}
.poster{position:absolute;left:184px;top:0;width:832px;height:1177px;overflow:hidden;
  background:
    radial-gradient(ellipse 420px 420px at 420px 360px,var(--white) 0%,rgba(255,255,255,.85) 40%,rgba(255,255,255,0) 100%),
    linear-gradient(200deg,var(--sky) 0%,#8fd3f2 30%,var(--sky-pale) 60%,var(--white) 85%);}
.headline-top{position:absolute;left:182px;top:82px;font-weight:800;font-size:61px;color:var(--teal);letter-spacing:1px;white-space:nowrap}
.headline-figure{position:absolute;left:150px;top:120px;font-weight:900;font-size:385px;line-height:1;color:var(--teal);letter-spacing:-14px;white-space:nowrap;
  -webkit-text-stroke:10px var(--white);paint-order:stroke fill;text-shadow:12px 14px 0 var(--teal-soft)}
.headline-main{position:absolute;left:158px;top:455px;font-weight:800;font-size:92px;line-height:82px;color:var(--grey);letter-spacing:-2px;white-space:nowrap}
.headline-sub{position:absolute;left:160px;top:640px;font-weight:700;font-size:48px;line-height:50px;color:var(--grey);white-space:nowrap}
.photo-street{position:absolute;left:0;top:790px;width:832px;height:280px;
  background:linear-gradient(180deg,rgba(255,255,255,0) 0%,#c9c8cc 25%,#b8b3ad 50%,#7fa06a 75%,#e9e7e3 90%,var(--white) 100%)}
.badge{position:absolute;left:430px;top:625px;width:234px;height:234px;border-radius:50%;
  background:radial-gradient(circle at 50% 20%,var(--red-light) 0%,var(--red) 55%,#7a1c22 100%);
  color:var(--white);text-align:center}
.badge-lead{display:block;margin-top:44px;font-weight:600;font-size:36px;line-height:36px}
.badge-value{display:block;font-weight:900;font-size:58px;line-height:60px;letter-spacing:-1px}
.badge-note{display:block;font-weight:600;font-size:18px;line-height:24px;margin-top:2px}
.contact{position:absolute;left:61px;top:1040px;color:#4a4a4f;font-size:13px;font-weight:600}
.contact-name{color:var(--teal);font-weight:800;font-size:13px;margin-bottom:8px}
.contact-row{display:flex;align-items:center;height:25px;white-space:nowrap}
.contact-item{display:flex;align-items:center;gap:11px;width:153px}
.contact-item.wide{width:auto}
.contact-item svg{width:13px;height:13px;fill:var(--teal);flex:none}
.brand{position:absolute;left:514px;top:1082px;font-weight:600;font-size:19px;color:var(--teal);letter-spacing:1px;white-space:nowrap}
.footer-bar{position:absolute;left:0;bottom:0;width:832px;height:17px;background:linear-gradient(90deg,var(--teal) 0 571px,#9a9a9e 571px 100%)}
</style>
</head>
<body>
<main class="poster">
  <div class="photo-street" role="img" aria-label="Foto einer sonnigen Wohnstraße mit hellen Einfamilienhäusern, Bäumen und Rasen"></div>

  <h1 class="headline-top">WIR SPENDEN</h1>
  <div class="headline-figure">5%</div>
  <div class="headline-main">UNSERER<br>PROVISION</div>
  <div class="headline-sub">FÜR IHREN<br>VEREIN</div>

  <div class="badge">
    <span class="badge-lead">Nur</span>
    <span class="badge-value">1,99%</span>
    <span class="badge-note">Maklercourtage</span>
  </div>

  <section class="contact">
    <div class="contact-name">HALVORSEN IMMOBILIEN</div>
    <div class="contact-row">
      <span class="contact-item wide"><svg viewBox="0 0 24 24"><path d="M12 2a7 7 0 0 0-7 7c0 5 7 13 7 13s7-8 7-13a7 7 0 0 0-7-7zm0 9.5A2.5 2.5 0 1 1 12 6.5a2.5 2.5 0 0 1 0 5z"/></svg>BIRKENALLEE 7 40210 SONNFELD</span>
    </div>
    <div class="contact-row">
      <span class="contact-item"><svg viewBox="0 0 24 24"><path d="M6.6 10.8a15 15 0 0 0 6.6 6.6l2.2-2.2a1 1 0 0 1 1-.25 11.4 11.4 0 0 0 3.6.57 1 1 0 0 1 1 1V20a1 1 0 0 1-1 1A17 17 0 0 1 3 4a1 1 0 0 1 1-1h3.5a1 1 0 0 1 1 1c0 1.25.2 2.45.57 3.6a1 1 0 0 1-.25 1z"/></svg>02100 555 21 09</span>
      <span class="contact-item wide"><svg viewBox="0 0 24 24"><path d="M3 5h18v14H3zm2 2v.5l7 4.5 7-4.5V7zm0 2.9V17h14V9.9l-7 4.5z"/></svg>INFO@HALVORSEN-IMMOBILIEN.DE</span>
    </div>
    <div class="contact-row">
      <span class="contact-item"><svg viewBox="0 0 24 24"><path d="M7 2h10a2 2 0 0 1 2 2v16a2 2 0 0 1-2 2H7a2 2 0 0 1-2-2V4a2 2 0 0 1 2-2zm0 3v13h10V5zm5 14.2a1 1 0 1 0 0 2 1 1 0 0 0 0-2z"/></svg>0150 555 678 90</span>
      <span class="contact-item wide"><svg viewBox="0 0 24 24"><path d="M12 2a10 10 0 1 0 0 20 10 10 0 0 0 0-20zm6.9 6h-3a15 15 0 0 0-1.3-3.9A8 8 0 0 1 18.9 8zM12 4c.8 1.2 1.5 2.5 1.9 4h-3.8c.4-1.5 1.1-2.8 1.9-4zM4.3 14a8 8 0 0 1 0-4h3.4a16 16 0 0 0 0 4zm.8 2h3a15 15 0 0 0 1.3 3.9A8 8 0 0 1 5.1 16zm3-8h-3a8 8 0 0 1 4.3-3.9A15 15 0 0 0 8.1 8zM12 20c-.8-1.2-1.5-2.5-1.9-4h3.8c-.4 1.5-1.1 2.8-1.9 4zm2.3-6H9.7a14 14 0 0 1 0-4h4.6a14 14 0 0 1 0 4zm.3 5.9a15 15 0 0 0 1.3-3.9h3a8 8 0 0 1-4.3 3.9zm1.7-5.9a16 16 0 0 0 0-4h3.4a8 8 0 0 1 0 4z"/></svg>WWW.HALVORSEN-IMMOBILIEN.DE</span>
    </div>
  </section>

  <div class="brand">HALVORSEN IMMOBILIEN</div>

  <div class="footer-bar"></div>
</main>
</body>
</html>
```